Offshore Energy Projects Management Consultancy needs a business card design

Logo available. We provide teams to deliver engineering consultancy, project management and delivery teams mainly in the offshore renewables sector. The company is all about bringing the right people to a project to deliver the scope.

The business card will be used for all staff.

The business card should be quite simple, vibrant and uncluttered but convey experience, enthusiasm and integration.

Target Market(s)

Energy Project Developers and Tier 1 construction companies

Contact Information for Business Card

Logo should be on the back of the card. I'm happy for the designer to play with the colour of the logo and background colour.

Front of the card should convey all the must have information in a clear and professional manner but without being overly traditional.

Colors

Designer to choose colors to be used in the design.

Requirements
Must have
• Land Line Tel Number, Mobile Tel Number, Email, business address, web address.

```html
<!DOCTYPE html>
<html lang="en">
<head>
<meta charset="utf-8">
<title>Tidewell Project Partners – Business Card</title>
<link rel="stylesheet" href="https://fonts.googleapis.com/css2?family=Montserrat:wght@400;500;600;700&display=swap">
<style>
  :root {
    --bg: #8e8e8e;
    --blue: #1473c0;
    --blue-deep: #0f66b2;
    --blue-light: #2ea6e6;
    --ink: #555a60;
    --white: #ffffff;
  }
  * { box-sizing: border-box; margin: 0; padding: 0; }
  html, body { width: 1200px; height: 930px; overflow: hidden; }
  body {
    background: radial-gradient(circle at 50% 40%, #b4b4b4, var(--bg));
    font-family: "Montserrat", sans-serif;
    position: relative;
  }
  .card {
    position: absolute;
    left: 280px;
    width: 640px;
    height: 366px;
    border-radius: 22px;
    overflow: hidden;
    box-shadow: 0 8px 22px rgba(0,0,0,.28);
  }
  /* Back */
  .card--back {
    top: 82px;
    background: linear-gradient(135deg, #2a8fd6, var(--blue-deep));
    display: flex;
    align-items: center;
    justify-content: center;
    gap: 16px;
  }
  .brand-dot {
    width: 26px; height: 26px; border-radius: 50%;
    background: var(--white);
  }
  .brand-name {
    font-weight: 700;
    font-size: 30px;
    letter-spacing: .5px;
    color: var(--white);
    text-transform: uppercase;
    line-height: 1.15;
  }
  /* Front */
  .card--front {
    top: 486px;
    background: var(--white);
  }
  .front-brand {
    position: absolute;
    left: 40px; top: 62px;
    display: flex; align-items: center; gap: 12px;
  }
  .front-brand .brand-dot { background: var(--blue); width: 20px; height: 20px; }
  .front-brand .brand-name { color: var(--ink); font-size: 21px; }
  .person {
    position: absolute;
    right: 40px; top: 102px;
    text-align: right;
  }
  .person__name { color: var(--blue); font-weight: 600; font-size: 26px; letter-spacing: .3px; }
  .person__title { color: var(--ink); font-size: 16px; margin-top: 2px; }
  .divider {
    position: absolute;
    left: 40px; right: 40px; top: 170px;
    height: 1.5px; background: var(--blue);
  }
  .address {
    position: absolute;
    right: 40px; top: 188px;
    text-align: right;
    color: var(--ink);
    font-size: 16px;
    line-height: 1.5;
  }
  .contact {
    position: absolute;
    left: 40px; top: 250px;
    list-style: none;
    color: var(--ink);
    font-size: 17px;
    line-height: 1.45;
  }
  .contact li { display: flex; align-items: center; gap: 10px; }
  .contact svg { width: 13px; height: 13px; fill: none; stroke: var(--blue); stroke-width: 2; }
  .contact .web-domain { color: var(--blue); }
  .wave { position: absolute; left: 0; bottom: 0; width: 640px; height: 366px; }
</style>
</head>
<body>
  <section class="card card--back" aria-label="Card back">
    <span class="brand-dot"></span>
    <span class="brand-name">Tidewell Project Partners</span>
  </section>

  <section class="card card--front" aria-label="Card front">
    <svg class="wave" viewBox="0 0 640 366" aria-hidden="true">
      <path d="M0,366 L0,352 C220,350 390,330 470,290 C540,255 590,246 640,242 L640,366 Z" fill="var(--blue)"/>
      <path d="M0,350 C220,346 385,322 462,282 C535,244 590,234 640,230" fill="none" stroke="var(--blue-light)" stroke-width="5"/>
      <path d="M0,346 C220,342 382,318 458,278 C532,240 588,229 640,225" fill="none" stroke="var(--white)" stroke-width="3"/>
    </svg>

    <div class="front-brand">
      <span class="brand-dot"></span>
      <span class="brand-name">Tidewell Project Partners</span>
    </div>

    <div class="person">
      <p class="person__name">DANIEL HARTLEY</p>
      <p class="person__title">President</p>
    </div>

    <div class="divider"></div>

    <address class="address" style="font-style:normal">
      2184 Harbor Lane<br>Easton, MD 21601
    </address>

    <ul class="contact">
      <li><svg viewBox="0 0 16 16"><path d="M4 1.5 L6.5 4.5 L5 6.5 C6 8.5 7.5 10 9.5 11 L11.5 9.5 L14.5 12 L12.5 14.5 C7 14 2 9 1.5 3.5 Z"/></svg>555-204-7719</li>
      <li><svg viewBox="0 0 16 16"><rect x="1.5" y="3.5" width="13" height="9"/><path d="M1.5 3.5 L8 9 L14.5 3.5"/></svg>info@tidewellpartners.com</li>
      <li><svg viewBox="0 0 16 16"><circle cx="8" cy="8" r="6.5"/><path d="M1.5 8 H14.5 M8 1.5 C5 5 5 11 8 14.5 C11 11 11 5 8 1.5"/></svg>www.<span class="web-domain">tidewellpartners</span>.com</li>
    </ul>
  </section>
</body>
</html>
```